Cardiology practice business card

We need a business card for our cardiology practice "Bellmoor Cardiology". We have a new logo, attached below. We like the colours in the logo - red and charcoal. The front of the business card will need to have the doctors name, address, phone number and email. The back will need to have space to write 2 appointment dates and times.

```html
<!DOCTYPE html>
<html lang="en">
<head>
<meta charset="utf-8">
<title>Bellmoor Cardiology – Business Card</title>
<link href="https://fonts.googleapis.com/css2?family=Lato:wght@400;700&display=swap" rel="stylesheet">
<style>
  :root {
    --red: #c0212d;
    --red-soft: #e8a3a8;
    --charcoal: #2b2b2b;
    --white: #ffffff;
    --ink: #111111;
  }
  html, body {
    margin: 0;
    padding: 0;
    overflow: hidden;
    background: var(--white);
  }
  .card {
    position: relative;
    width: 1200px;
    height: 777px;
    overflow: hidden;
    background: var(--white);
    font-family: "Lato", "Helvetica Neue", Arial, sans-serif;
  }
  .card__dark-panel {
    position: absolute;
    left: 470px;
    top: 0;
    width: 730px;
    height: 777px;
    background: var(--charcoal);
  }
  .brand-name {
    position: absolute;
    left: 80px;
    top: 128px;
    margin: 0;
    font-size: 31px;
    font-weight: 700;
    color: var(--red);
    letter-spacing: 0.5px;
  }
  .heartbeat-art {
    position: absolute;
    left: 207px;
    top: 252px;
    width: 263px;
    height: 270px;
    background: linear-gradient(90deg, var(--red-soft) 0%, var(--red) 100%);
  }
  .divider-line {
    position: absolute;
    left: 0;
    top: 0;
  }
  .doctor {
    position: absolute;
    left: 611px;
    top: 168px;
    color: var(--white);
  }
  .doctor__name {
    margin: 0;
    font-size: 52px;
    font-weight: 700;
    line-height: 1.1;
    padding-bottom: 2px;
    border-bottom: 5px solid var(--red);
    width: 357px;
    white-space: nowrap;
  }
  .doctor__role {
    margin: 12px 0 0;
    font-size: 25px;
    font-weight: 400;
    letter-spacing: 0.3px;
  }
  .contacts {
    position: absolute;
    left: 643px;
    top: 480px;
    margin: 0;
    padding: 0;
    list-style: none;
    color: var(--white);
    font-size: 28.5px;
  }
  .contacts__item {
    display: flex;
    align-items: center;
    height: 40px;
    margin-bottom: 21px;
    white-space: nowrap;
  }
  .contacts__icon {
    width: 36px;
    height: 36px;
    margin-right: 32px;
    flex: none;
  }
</style>
</head>
<body>
<main class="card">
  <div class="card__dark-panel"></div>

  <p class="brand-name">Bellmoor Cardiology</p>

  <div class="heartbeat-art" role="img" aria-label="Red heartbeat pulse illustration"></div>

  <svg class="divider-line" width="1200" height="777" viewBox="0 0 1200 777" aria-hidden="true">
    <polygon fill="var(--ink)" points="470,375 990,378 990,379 470,386"/>
  </svg>

  <section class="doctor">
    <h1 class="doctor__name">Name Surname</h1>
    <p class="doctor__role">GENERAL SURGEON</p>
  </section>

  <ul class="contacts">
    <li class="contacts__item">
      <svg class="contacts__icon" viewBox="0 0 24 24" aria-hidden="true">
        <path fill="var(--red)" d="M6.6 10.8a15.1 15.1 0 0 0 6.6 6.6l2.2-2.2c.3-.3.7-.4 1-.2 1.1.4 2.3.6 3.6.6.6 0 1 .4 1 1V20c0 .6-.4 1-1 1A17 17 0 0 1 3 4c0-.6.4-1 1-1h3.5c.6 0 1 .4 1 1 0 1.3.2 2.5.6 3.6.1.3 0 .7-.2 1z"/>
      </svg>
      <span>(00)123.456.789</span>
    </li>
    <li class="contacts__item">
      <svg class="contacts__icon" viewBox="0 0 24 24" aria-hidden="true">
        <rect x="2" y="5" width="20" height="14" rx="1" fill="var(--red)"/>
        <path d="M3 6l9 7 9-7M3 18l7-6M21 18l-7-6" fill="none" stroke="var(--charcoal)" stroke-width="1.3"/>
      </svg>
      <span>mail@example.com</span>
    </li>
    <li class="contacts__item">
      <svg class="contacts__icon" viewBox="0 0 24 24" aria-hidden="true">
        <g fill="none" stroke="var(--red)" stroke-width="2">
          <circle cx="12" cy="12" r="9.5"/>
          <ellipse cx="12" cy="12" rx="4" ry="9.5"/>
          <path d="M2.5 12h19M4 7h16M4 17h16"/>
        </g>
      </svg>
      <span>www.example.com</span>
    </li>
    <li class="contacts__item">
      <svg class="contacts__icon" viewBox="0 0 24 24" aria-hidden="true">
        <path fill="var(--red)" d="M12 1.5a7.5 7.5 0 0 0-7.5 7.5c0 5.6 7.5 13.5 7.5 13.5s7.5-7.9 7.5-13.5A7.5 7.5 0 0 0 12 1.5zm0 10.5a3 3 0 1 1 0-6 3 3 0 0 1 0 6z"/>
      </svg>
      <span>Street adress, city, country</span>
    </li>
  </ul>
</main>
</body>
</html>
```